Bramblewick Affairs Web Design Project

This is a bit of a challenging request. Bramblewick Affairs (event planning) and ORB Gala Hireworks (event equipment rental), operate in the Northern Virginia area and we are in the process of marketing ourselves heavily as a "on stop celebration shop". Our customers range from large music festivals to smaller corporate functions. We are seeking to integrate two companies under one umbrella, our event planning company which also offers catering services " Bramblewick Affair, LLC" with our event rental equipment company "ORB Gala Hireworks." Both have new logos created through Pixel Harbor. I would like to have one portal that provides access to both companies and maintain the party rental URL as a stand alone to remain accessible to our loyal customers if possible. The only website that exist today is ORB Gala Hireworks with the URL (www.orbgalahub.example), which needs a complete redesign, as it is very antiquated. This URL should still be able to stand on its own as well as integrated/accessible into the new overall parent company BRamblewick Affairs/ Our goal is to is to communicate to our customers that we are energetic, modern company with fresh celebration ideas and the hardware to go with it. There are numerous photos that need to be uploaded to the rental part of site. We will need to be able to update and make changes to photos without outside support.

Reason: I am changing the project to being a non-refundable and hope to get more submissions.

Target Market(s)

A very broad range of customers, from large rock festivals, to small country weddings and corporate functions

Industry/Entity Type

Event Planning

Requirements
Must have
• Must Have:
- - Ability to add and update photos without external support
-Modern interface ( look and feel)
-Easy user centered design
- multiple sections ( tabs) such as , Home, Event Planning, Catering, Galleries, Venues, Contact Us
Nice to have
• - ability to place event rental orders online

```html
<!DOCTYPE html>
<html lang="en">
<head>
<meta charset="utf-8">
<title>Bramblewick Affairs — Home</title>
<link href="https://fonts.googleapis.com/css2?family=Arimo:wght@400;700&family=Almendra:wght@700&display=swap" rel="stylesheet">
<style>
  :root {
    --page-bg: #f7f7f6;
    --brand-orange: #f07030;
    --brand-orange-deep: #e8452a;
    --brand-amber: #fbb03b;
    --brand-purple: #5b3d9a;
    --text-dark: #111111;
    --white: #ffffff;
    --field-border: #a9a9a9;
    --field-text: #555555;
    --icon-grey: #9aa3ab;
  }
  * { box-sizing: border-box; margin: 0; padding: 0; }
  html, body { width: 1200px; height: 1000px; overflow: hidden; }
  body {
    position: relative;
    background: var(--page-bg);
    font-family: "Arimo", Arial, sans-serif;
    color: var(--text-dark);
  }
  .corner-accent {
    position: absolute;
    left: -330px; top: -120px;
    width: 560px; height: 520px;
    border-radius: 50%;
    background: radial-gradient(circle at 70% 55%, var(--brand-orange-deep) 0%, var(--brand-orange) 45%, var(--brand-amber) 100%);
  }
  .site-search {
    position: absolute;
    left: 496px; top: 38px;
    width: 209px; height: 30px;
    border: 1px solid var(--field-border);
    border-radius: 8px;
    background: var(--white);
    display: flex; align-items: center;
  }
  .site-search svg { margin-left: 8px; }
  .site-search span {
    margin-left: 34px;
    font-size: 12.5px;
    color: var(--field-text);
  }
  .brand-mark {
    position: absolute;
    left: 350px; top: 112px;
    height: 86px;
    display: flex; align-items: center;
  }
  .brand-mark .dot {
    width: 80px; height: 80px;
    border-radius: 50%;
    background: var(--brand-orange);
    margin-right: 40px;
  }
  .brand-mark .name {
    font-size: 40px;
    font-weight: 700;
    color: var(--brand-purple);
    letter-spacing: -0.5px;
    white-space: nowrap;
  }
  .main-nav {
    position: absolute;
    left: 219px; top: 267px;
    width: 768px;
    display: flex; justify-content: space-between;
    font-size: 14.5px;
  }
  .main-nav a { color: var(--brand-purple); text-decoration: none; }
  .main-nav a.is-current { color: var(--brand-orange); }
  .hero-slide {
    position: absolute;
    left: 219px; top: 306px;
    width: 768px; height: 344px;
    background:
      radial-gradient(ellipse 52% 62% at 50% 72%, #fff3c4 0%, #f7c95a 30%, #c7882b 58%, rgba(60,30,10,0.6) 80%, transparent 100%),
      linear-gradient(#050505 0%, #0a0808 60%, #3a1a10 100%);
  }
  .slide-counter {
    position: absolute;
    left: 540px; top: 655px;
    width: 134px;
    display: flex; align-items: center; justify-content: space-between;
  }
  .slide-counter .count {
    font-family: "Almendra", Georgia, serif;
    font-size: 38px;
    font-weight: 700;
    color: var(--brand-orange);
    line-height: 1;
  }
  .intro-copy {
    position: absolute;
    left: 255px; top: 700px;
    width: 692px;
    font-size: 12.6px;
    line-height: 15.2px;
  }
  .footer-band {
    position: absolute;
    left: 219px; top: 864px;
    width: 768px; height: 45px;
    background: var(--brand-orange);
    display: flex; justify-content: center; align-items: center;
    gap: 16px;
    font-size: 11px;
  }
  .footer-band a { color: var(--white); text-decoration: none; }
  .social-links {
    position: absolute;
    left: 252px; top: 928px;
    display: flex;
  }
  .social-links span {
    width: 50px; height: 50px;
    border-radius: 50%;
    background: var(--icon-grey);
    border: 2px solid #d8dcdf;
    margin-right: -8px;
  }
  .footer-brand {
    position: absolute;
    left: 575px; top: 926px;
    height: 40px;
    display: flex; align-items: center;
  }
  .footer-brand .dot {
    width: 34px; height: 34px; border-radius: 50%;
    background: var(--brand-orange); margin-right: 8px;
  }
  .footer-brand .name {
    font-size: 16px; font-weight: 700; color: var(--brand-purple); line-height: 1;
    white-space: nowrap;
  }
  .partner-brand {
    position: absolute;
    left: 817px; top: 924px;
    display: flex; align-items: center;
  }
  .partner-brand .dot {
    width: 52px; height: 52px; border-radius: 50%;
    background: var(--brand-purple); margin-right: 8px;
  }
  .partner-brand .name {
    width: 115px;
    font-size: 15px; font-weight: 700; color: var(--brand-orange); line-height: 1.1;
  }
</style>
</head>
<body>
  <div class="corner-accent" aria-hidden="true"></div>

  <div class="site-search">
    <svg width="22" height="22" viewBox="0 0 22 22" aria-hidden="true">
      <circle cx="9" cy="9" r="6.5" fill="none" stroke="#333" stroke-width="2.6"/>
      <line x1="13.8" y1="13.8" x2="20" y2="20" stroke="#333" stroke-width="3.4" stroke-linecap="round"/>
    </svg>
    <span>Search Here...</span>
  </div>

  <header class="brand-mark">
    <span class="dot" aria-hidden="true"></span>
    <span class="name">Bramblewick Affairs</span>
  </header>

  <nav class="main-nav">
    <a class="is-current" href="#">HOME</a>
    <a href="#">EVENT PLANNING</a>
    <a href="#">CATERING</a>
    <a href="#">GALLERIES</a>
    <a href="#">VENUES</a>
    <a href="#">CONTACT US</a>
  </nav>

  <div class="hero-slide" role="img" aria-label="Photo of an illuminated wedding stage with golden fan-shaped drapery, flowers and chairs at night"></div>

  <div class="slide-counter">
    <svg width="24" height="24" viewBox="0 0 24 24" aria-label="Previous slide"><polygon points="2,12 22,2 22,22" fill="var(--brand-orange)"/></svg>
    <span class="count">1/8</span>
    <svg width="24" height="24" viewBox="0 0 24 24" aria-label="Next slide"><polygon points="22,12 2,2 2,22" fill="var(--brand-orange)"/></svg>
  </div>

  <p class="intro-copy">Lorem ipsum dolor sit amet, consectetur adipisicing elit, sed do eiusmod tempor incididunt ut labore et dolore magna aliqua. Ut enim ad minim veniam, quis nostrud exercitation ullamco laboris nisi ut aliquip ex ea commodo consequat. Duis aute irure dolor in reprehenderit in voluptate velit esse cillum dolore eu fugiat nulla pariatur. Excepteur sint occaecat cupidatat non proident, sunt in culpa qui officia deserunt mollit anim id est laborum. Sed ut perspiciatis unde omnis iste natus error sit voluptatem accusantium doloremque laudantium. Lorem ipsum dolor sit amet, consectetur adipisicing elit, sed do eiusmod tempor incididunt ut labore et dolore magna aliqua. Ut enim ad minim veniam, quis nostrud exercitation ullamco laboris nisi ut aliquip ex ea commodo consequat. Duis aute irure dolor in reprehenderit in voluptate velit esse cillum dolore eu fugiat nulla pariatur. Excepteur sint occaecat cupidatat non proident, sunt in culpa qui officia deserunt mollit anim id est laborum. Sed ut perspiciatis unde omnis iste natus error sit voluptatem accusantium doloremque laudantium.</p>

  <nav class="footer-band">
    <a href="#">HOME</a>
    <a href="#">EVENT PLANNING</a>
    <a href="#">CATERING</a>
    <a href="#">GALLERIES</a>
    <a href="#">VENUES</a>
    <a href="#">CONTACT US</a>
  </nav>

  <div class="social-links" aria-label="Social media links">
    <span></span><span></span><span></span><span></span>
  </div>

  <div class="footer-brand">
    <span class="dot" aria-hidden="true"></span>
    <span class="name">Bramblewick Affairs</span>
  </div>

  <div class="partner-brand">
    <span class="dot" aria-hidden="true"></span>
    <span class="name">ORB Gala Hireworks</span>
  </div>
</body>
</html>
```